Complete web site needs re-design

Webpage will include one product labeled Talvex (™) .
This webpage must be viewable on Mobile devices and all common browsers - Safari, Chrome, IE, Mozilla Firefox..

Design will be similar to that of
http://www.morvellworks.example/aviation/
or
http://www.plexory.example/site-layout/view/html/482?utm_content=qx_html_ktp_demo_3_7TrialItem&utm_medium=layout_strip&utm_campaign=qx_ktp&utm_source=opensitelayouts&experiment_id=qx_html_ktp_demo_3_7TrialItem&utm_term=meetups

- in that it will be simple and introduce our product.

Website will be ready to accept shop till when the product is released. The integration of this feature will also go to the winner.

Tabs for information will be provided for "About, Features, Where to buy"

The page should include one vidqueue as a sample of the product. this will be linked to the following video http://www.vidqueue.example/watch?v=kRT519pz8va.

Good luck applicants!

Target Market(s)

The target audience will be sport enthusiasts of all walks (from car racing to skydiving) looking to supplement their zip-cam camera with an extra mount.

Industry/Entity Type

Events

Font styles to use
Other font styles liked:
• Helvetica

Colors
d5d5d5
919191
f6f6f6
c8c8c8
ebebeb
5c5c5c
aaaaaa
ffffff

Requirements
Must have
• Front page is introducing our "Talvex" product. Search engines need to identify "Extreme, POV, ZipCam, Self,Levelling, Auto, Stabilising, Motocross, surfing, Moto X, Wake, Kite, Boarding, Skydiving, Racing, Bike, Aerobatic, blue stag, Mount,Ski, downhill, snow, base jumping," etc..

The mount is designed to hold a zip-cam camera in all and any extreme situations. Ensure the search returns this .

An "about" and "contact" shall be provided on the company logo.

Tabs for information will be provided for "About, Features, Where to buy" - This information will be provided by us, once the webpage is complete.

Font is "Helvetica"
Nice to have
• Prepare the page flow so multiple variations of the product, and accessories can be added easily. As mentioned earlier, a shopping cart will be required (ShopTill) in the near future.

As you can see the company logo is designed to be cut into the product. It would be nice if it had an embossed effect to look the same. This goes for the "Talvex" logo also.

```html
<!DOCTYPE html>
<html lang="en">
<head>
<meta charset="utf-8">
<title>Vantrel – Talvex Ready To Fly</title>
<meta name="description" content="Talvex self-levelling, auto-stabilising ZipCam mount for extreme POV: motocross, surfing, skydiving, racing, ski, downhill, base jumping.">
<link rel="stylesheet" href="https://fonts.googleapis.com/css2?family=Open+Sans:wght@300;400;600&display=swap">
<style>
:root{
  --blue:#1fb2ef;
  --blue-dark:#0f95d2;
  --charcoal:#343434;
  --charcoal-dark:#2a2a2a;
  --text:#5c5c5c;
  --muted:#919191;
  --grey-mid:#aaaaaa;
  --line:#c8c8c8;
  --grey-light:#d5d5d5;
  --pale:#f6f6f6;
  --pale-2:#ebebeb;
  --white:#ffffff;
}
*{box-sizing:border-box;margin:0;padding:0}
html,body{width:960px;height:1200px;overflow:hidden;background:var(--white);font-family:"Open Sans",Helvetica,Arial,sans-serif;color:var(--text)}
.page{position:absolute;left:50px;top:14px;width:857px;height:1172px;background:linear-gradient(var(--pale),var(--white) 45%)}
.site{position:absolute;left:29px;top:20px;width:800px;background:var(--white);box-shadow:0 0 18px rgba(0,0,0,.08)}
.nav{display:flex;height:30px;background:var(--blue);border-radius:3px 3px 0 0;padding-left:4px;border-bottom:2px solid var(--blue-dark)}
.nav a{width:104px;color:var(--white);text-decoration:none;font-size:10px;text-align:center;line-height:30px;border-right:1px solid var(--blue-dark)}
.nav a.active{background:#27b6f2;box-shadow:inset 0 -2px 0 #0a86c0;line-height:34px}
.header{height:79px;background:var(--charcoal);display:flex;align-items:center;justify-content:space-between;padding:0 25px 0 52px}
.brand{font-size:38px;font-weight:600;color:var(--muted);letter-spacing:1px}
.call{font-size:18px;color:var(--pale-2);font-weight:300}
.call span{color:var(--blue)}
.hero{height:307px;background:radial-gradient(ellipse at 50% 45%,#d9d9de 0%,#a9a9b1 35%,#6e6e78 100%);position:relative}
.slider{position:absolute;left:348px;top:296px;width:103px;height:20px;background:var(--blue);border-radius:3px;display:flex;align-items:center;justify-content:space-between;padding:0 8px}
.dots{display:flex;gap:7px;border-left:1px solid var(--blue-dark);border-right:1px solid var(--blue-dark);padding:0 9px}
.dots i{width:6px;height:6px;border-radius:50%;background:#dff3fc;display:block}
.dots i.on{background:#111}
.intro{padding:38px 24px 0}
.intro h1{font-size:32px;font-weight:300;text-align:center;color:var(--text);letter-spacing:.5px}
.rule{border-top:1px dotted var(--line);margin-top:20px}
.features{display:flex;gap:30px;margin-top:23px}
.feature{width:165px}
.thumb{height:76px;display:block}
.feature h2{font-size:21px;font-weight:300;margin:13px 0 11px;color:var(--text);letter-spacing:.6px}
.feature p{font-size:9.2px;line-height:11.8px;color:var(--text);letter-spacing:.35px;padding-right:4px}
.btn{display:inline-block;margin-top:11px;background:var(--blue);color:var(--white);font-size:10px;padding:0 11px;line-height:20px;border-radius:2px;text-decoration:none;box-shadow:0 2px 0 #0d85be}
.projects{display:flex;gap:31px;margin-top:19px;padding-bottom:33px}
.project{width:229px;background:var(--white);box-shadow:0 0 5px rgba(0,0,0,.15)}
.project .thumb{height:105px}
.project h3{font-size:13px;font-weight:300;color:var(--blue);margin:12px 16px 0;padding-bottom:5px;border-bottom:1px dotted var(--line)}
.project p{font-size:9px;line-height:11.5px;color:var(--text);margin:9px 22px 17px 16px;letter-spacing:.3px}
.tags{background:var(--pale);font-size:7.5px;color:var(--muted);padding:9px 16px 10px}
.img-drone{background:radial-gradient(ellipse at 50% 45%,#d7d7dc,#8d8d97 70%,#6d6d77)}
.img-mount{background:linear-gradient(135deg,#f2f2f2 30%,#d5d5d5 60%,#7c7c78)}
.img-board{background:radial-gradient(ellipse at 55% 45%,#9a9a9a,#e9e9e9 45%,#fafafa)}
.img-helmet{background:linear-gradient(100deg,#1c2424 55%,#4a4640 80%,#8a6a4a)}
.footer{position:absolute;left:0;top:1060px;width:857px;height:112px;background:linear-gradient(var(--charcoal),var(--charcoal-dark));border-top:2px solid var(--blue);display:flex;justify-content:space-between;align-items:center;padding:0 56px 0 53px}
.footer .copy{font-size:9px;color:var(--pale-2)}
.footer nav{display:flex;gap:9px}
.footer nav a{font-size:8.5px;color:#7a7a7a;text-decoration:none}
</style>
</head>
<body>
<div class="page">
  <div class="site">
    <nav class="nav">
      <a class="active" href="#">About Us</a>
      <a href="#">Where to find</a>
      <a href="#">Auto Pilots</a>
      <a href="#">Talvex AX4</a>
      <a href="#">Support</a>
      <a href="#">Log In</a>
      <a href="#">Cart</a>
    </nav>
    <header class="header">
      <div class="brand">Vantrel</div>
      <div class="call"><span>Call</span> 0.000.000.0000</div>
    </header>
    <section class="hero" role="img" aria-label="White quadcopter carrying the Talvex camera mount on a grey studio backdrop">
      <div class="slider">
        <svg width="8" height="10" viewBox="0 0 8 10"><path d="M6 1 2 5l4 4" stroke="#fff" stroke-width="2" fill="none"/></svg>
        <div class="dots"><i></i><i></i><i class="on"></i></div>
        <svg width="8" height="10" viewBox="0 0 8 10"><path d="m2 1 4 4-4 4" stroke="#fff" stroke-width="2" fill="none"/></svg>
      </div>
    </section>
    <main class="intro">
      <h1>Ready To Fly</h1>
      <div class="rule"></div>
      <section class="features">
        <article class="feature">
          <div class="thumb img-drone" role="img" aria-label="Quadcopter drone"></div>
          <h2>Innovation</h2>
          <p>Pellentesque tristique volutpat nunc, id rhoncus augue tristique sed. In at nisl nulla, et vestibulum risus.</p>
          <a class="btn" href="#">Read More</a>
        </article>
        <article class="feature">
          <div class="thumb img-mount" role="img" aria-label="Action camera on a helmet mount"></div>
          <h2>Support</h2>
          <p>Pellentesque tristique volutpat nunc, id rhoncus augue tristique sed. In at nisl nulla, et vestibulum risus.</p>
          <a class="btn" href="#">Read More</a>
        </article>
        <article class="feature">
          <div class="thumb img-board" role="img" aria-label="Flight controller board with highlighted components"></div>
          <h2>Partners</h2>
          <p>Pellentesque tristique volutpat nunc, id rhoncus augue tristique sed. In at nisl nulla, et vestibulum risus.</p>
          <a class="btn" href="#">Read More</a>
        </article>
        <article class="feature">
          <div class="thumb img-helmet" role="img" aria-label="Camera mounted on a dark helmet"></div>
          <h2>Careers</h2>
          <p>Pellentesque tristique volutpat nunc, id rhoncus augue tristique sed. In at nisl nulla, et vestibulum risus.</p>
          <a class="btn" href="#">Read More</a>
        </article>
      </section>
      <div class="rule"></div>
      <section class="projects">
        <article class="project">
          <div class="thumb img-drone" role="img" aria-label="Quadcopter drone"></div>
          <h3>Sample project</h3>
          <p>Lorem ipsum dolor sit amet, consectetur adipiscing elit. Quis que nibh metus, feugiat et</p>
          <div class="tags">business, corporate</div>
        </article>
        <article class="project">
          <div class="thumb img-board" role="img" aria-label="Flight controller board with highlighted components"></div>
          <h3>Career &amp; Education</h3>
          <p>Lorem ipsum dolor sit amet, consectetur adipiscing elit. Quis que nibh metus, feugiat et</p>
          <div class="tags">web-design, success</div>
        </article>
        <article class="project">
          <div class="thumb img-helmet" role="img" aria-label="Camera mounted on a dark helmet"></div>
          <h3>Sample project</h3>
          <p>Lorem ipsum dolor sit amet, consectetur adipiscing elit. Quis que nibh metus, feugiat et</p>
          <div class="tags">business, corporate</div>
        </article>
      </section>
    </main>
  </div>
  <footer class="footer">
    <div class="copy">Vantrel © 2013-2014 All Rights Reserved.</div>
    <nav><a href="#">Home</a><a href="#">Where to Find</a><a href="#">Support</a><a href="#">Products</a><a href="#">Disclaimer</a></nav>
  </footer>
</div>
</body>
</html>
```